E-commerce Website needs category banner

What we need for our category banner is a clean, predominately black design that showcases the product we are trying to sell (currently only 1), and a few subtle gradients that follow the pattern set by previous designs.

An example will be provided to showcase what we want.

It needs to say:
Outdoor Motion Detection Lighting in large, clear font similar to the example provided.
Updates

Please ensure dimensions are as follows: 980x300

Target Market(s)

Senior citizens, businesses, homeowners, families, etc

Industry/Entity Type

Product

Font styles to use
Sans Serif

Requirements
Must have
• It needs to say:
Outdoor Motion Detection Lighting in large, clear font similar to the example provided
980x300 is the required size!
Should not have
• Too much going on- clean and simple please (no crazy fonts, logos, etc)

```html
<!DOCTYPE html>
<html lang="en">
<head>
<meta charset="UTF-8">
<title>Outdoor Motion Detection Lighting</title>
<link rel="stylesheet" href="https://fonts.googleapis.com/css2?family=Montserrat:wght@700&display=swap">
<style>
  :root {
    --bg-light: #5c5c5c;
    --bg-mid: #3f3f3f;
    --bg-dark: #222222;
    --headline: #ececec;
    --headline-shade: rgba(0, 0, 0, 0.65);
    --lamp-white-hi: #f4f4f2;
    --lamp-white-lo: #b9b9b6;
    --lamp-dark-hi: #5a5f63;
    --lamp-dark-lo: #24272a;
  }
  html, body {
    margin: 0;
    padding: 0;
    width: 1200px;
    height: 469px;
    overflow: hidden;
    background: var(--bg-dark);
  }
  .banner {
    position: relative;
    width: 1200px;
    height: 469px;
    overflow: hidden;
    background:
      radial-gradient(ellipse 70% 90% at 62% 40%, var(--bg-light) 0%, var(--bg-mid) 45%, var(--bg-dark) 100%);
  }
  .headline {
    margin: 0;
    font-family: "Montserrat", sans-serif;
    font-weight: 700;
    color: var(--headline);
    text-shadow: 2px 3px 4px var(--headline-shade), 0 0 1px #ffffff;
  }
  .headline-line {
    position: absolute;
    left: 37px;
    display: block;
    line-height: 1;
    white-space: nowrap;
    transform-origin: left top;
  }
  .line-outdoor   { top: 30px;  font-size: 100px; transform: scaleX(0.98); }
  .line-motion    { top: 116px; font-size: 150px; transform: scaleX(0.76); }
  .line-detection { top: 252px; font-size: 95px;  transform: scaleX(0.84); }
  .line-lighting  { top: 330px; left: 78px; font-size: 136px; transform: scaleX(0.67); }

  .product {
    position: absolute;
  }
  .product-white {
    left: 625px;
    top: 67px;
    width: 232px;
    height: 337px;
    border-radius: 48% 48% 40% 40% / 36% 36% 44% 44%;
    background: radial-gradient(circle at 40% 30%, var(--lamp-white-hi) 0%, var(--lamp-white-lo) 80%);
  }
  .product-dark {
    left: 870px;
    top: 31px;
    width: 287px;
    height: 373px;
    border-radius: 42% 30% 36% 40% / 30% 26% 40% 44%;
    background: radial-gradient(circle at 35% 30%, var(--lamp-dark-hi) 0%, var(--lamp-dark-lo) 80%);
  }
</style>
</head>
<body>
  <main class="banner">
    <h1 class="headline">
      <span class="headline-line line-outdoor">OUTDOOR</span>
      <span class="headline-line line-motion">MOTION</span>
      <span class="headline-line line-detection">DETECTION</span>
      <span class="headline-line line-lighting">LIGHTING</span>
    </h1>
    <div class="product product-white" role="img" aria-label="White wireless motion sensor spotlight on a wall mount"></div>
    <div class="product product-dark" role="img" aria-label="Dark brown wireless motion sensor spotlight with twin LEDs on a wall mount"></div>
  </main>
</body>
</html>
```